Business Cards and others
Business cards, stationery, Powerpoint template and E-mail Header and Footer
Professional
Darian Lutrell
CEO
4827 Thornwick Ln
Harwick VT 05417
darian@velmorix.com
www.velmorix.com

```html
<!DOCTYPE html>
<html lang="en">
<head>
<meta charset="utf-8">
<title>Velmorix Business Card</title>
<link href="https://fonts.googleapis.com/css2?family=Open+Sans:wght@400;600;700&display=swap" rel="stylesheet">
<style>
  :root {
    --backdrop: #2b2b2d;
    --card: #ffffff;
    --brand-blue: #2ea3dd;
    --brand-blue-light: #6cc4ee;
    --brand-blue-dark: #1b86c4;
    --text-grey: #7a7d80;
  }
  * { margin: 0; padding: 0; box-sizing: border-box; }
  html, body {
    width: 1200px; height: 852px; overflow: hidden;
    background: var(--backdrop);
    font-family: "Open Sans", Arial, sans-serif;
  }
  .business-card {
    position: absolute; left: 100px; top: 141px;
    width: 1000px; height: 571px;
    background: var(--card);
    border-radius: 34px;
    overflow: hidden;
  }
  .brand-band {
    position: absolute; left: 70px; top: 0;
    width: 84px; height: 100%;
    background: linear-gradient(90deg, var(--brand-blue-dark), var(--brand-blue-light) 55%, var(--brand-blue));
  }
  .brand-mark {
    position: absolute; left: 52px; top: 58px;
    width: 120px; height: 120px; border-radius: 50%;
    background: var(--brand-blue);
    border: 8px solid #ffffff;
    box-shadow: 0 0 0 2px var(--brand-blue-light);
  }
  .brand-name {
    position: absolute; left: 188px; top: 78px;
    font-size: 66px; font-weight: 600; letter-spacing: -1px;
    color: var(--brand-blue);
  }
  .address {
    position: absolute; left: 196px; top: 266px;
    font-size: 20px; line-height: 30px; color: var(--text-grey);
  }
  .holder {
    position: absolute; right: 78px; top: 266px; text-align: right;
  }
  .holder-name { font-size: 28px; font-weight: 700; color: var(--brand-blue); }
  .holder-title { font-size: 17px; color: var(--text-grey); margin-top: 2px; }
  .contact-list {
    position: absolute; left: 196px; top: 370px; list-style: none;
    font-size: 20px; line-height: 34px; color: var(--text-grey);
  }
  .band-icon { position: absolute; left: 97px; }
</style>
</head>
<body>
  <section class="business-card">
    <div class="brand-band"></div>
    <div class="brand-mark"></div>
    <div class="brand-name">Velmorix</div>

    <svg class="band-icon" style="top:276px" width="30" height="30" viewBox="0 0 24 24" aria-hidden="true">
      <path d="M3 12 L12 4 L21 12 H18 V20 H14 V15 H10 V20 H6 V12 Z" fill="#fff"/>
    </svg>
    <svg class="band-icon" style="top:378px" width="30" height="30" viewBox="0 0 24 24" aria-hidden="true">
      <path d="M6 3 L9 3 L10.5 8 L8.5 9.5 C9.5 12 12 14.5 14.5 15.5 L16 13.5 L21 15 L21 18 C21 19.5 19.5 21 18 21 C10 20 4 14 3 6 C3 4.5 4.5 3 6 3 Z" fill="#fff"/>
    </svg>
    <svg class="band-icon" style="top:412px" width="30" height="30" viewBox="0 0 24 24" aria-hidden="true">
      <path d="M6 3 L9 3 L10.5 8 L8.5 9.5 C9.5 12 12 14.5 14.5 15.5 L16 13.5 L21 15 L21 18 C21 19.5 19.5 21 18 21 C10 20 4 14 3 6 C3 4.5 4.5 3 6 3 Z" fill="#fff"/>
    </svg>
    <svg class="band-icon" style="top:446px" width="30" height="30" viewBox="0 0 24 24" aria-hidden="true">
      <rect x="7" y="2" width="10" height="20" rx="2" fill="#fff"/><rect x="9" y="5" width="6" height="11" fill="#2ea3dd"/>
    </svg>
    <svg class="band-icon" style="top:480px" width="30" height="30" viewBox="0 0 24 24" aria-hidden="true">
      <rect x="3" y="6" width="18" height="12" rx="1.5" fill="#fff"/><path d="M3.5 6.5 L12 13 L20.5 6.5" stroke="#2ea3dd" stroke-width="1.6" fill="none"/>
    </svg>
    <svg class="band-icon" style="top:514px" width="30" height="30" viewBox="0 0 24 24" aria-hidden="true">
      <circle cx="12" cy="12" r="8.5" fill="none" stroke="#fff" stroke-width="2"/><path d="M3.5 12 H20.5 M12 3.5 C8 8 8 16 12 20.5 M12 3.5 C16 8 16 16 12 20.5" stroke="#fff" stroke-width="1.5" fill="none"/>
    </svg>

    <div class="address">4827 Thornwick Ln<br>Harwick VT 05417</div>

    <div class="holder">
      <div class="holder-name">Darian Lutrell</div>
      <div class="holder-title">CEO</div>
    </div>

    <ul class="contact-list">
      <li>855-610-4471</li>
      <li>4435028816</li>
      <li>9172093574</li>
      <li>darian@velmorix.com</li>
      <li>www.velmorix.com</li>
    </ul>
  </section>
</body>
</html>
```